Candle Box & Belly Band Design

Design Candle Box for Soy Candles along with a belly band design that can be used on off the shelf coloured boxes. It is for a premium brand of candle - so i want the packaging to reflect this. I have included must haves below.

The candle boxes will be a few different sizes, but for the purpose of the design it would be something like a cube 12 x 12 x 12 cms

The belly band for standard boxes to be something like 5cm wide on a 12 x 12 x 12cms cube box that goes all the way around the top to the bottom - holding the lid on and providing all the relevant information. Example of box with belly band uploaded

Our company Name : Fern & Isla - our logo is uploaded

Target Market(s)

Premium Candle Buyers

Colors

Designer to choose colors to be used in the design.

Requirements
Must have
• Must have our logo - our logo can be in any colour
• Must state:
• Soy Candle, Hand Poured, Made in Melbourne,
• A space for the fragrance, size and burn time.
• For this project use Lime, Coconut & Elderfllower, 300grams, 50 Hour burn Time

```html
<!DOCTYPE html>
<html lang="en">
<head>
<meta charset="utf-8">
<title>Fern &amp; Isla – Soy Candle Box Dieline</title>
<link rel="stylesheet" href="https://fonts.googleapis.com/css2?family=Roboto:wght@300;400;500&family=Nothing+You+Could+Do&display=swap">
<style>
  :root {
    --paper: #ffffff;
    --cut-line: #e8262b;
    --charcoal: #3d393a;
    --ink: #231f20;
    --lime: #bebd30;
    --muted: #8a8a8a;
    --on-dark: #ffffff;
  }
  * { margin: 0; padding: 0; box-sizing: border-box; }
  html, body {
    width: 1200px; height: 666px; overflow: hidden;
    background: var(--paper);
  }
  .sheet { position: relative; width: 1200px; height: 666px; }
  .dieline { position: absolute; left: 0; top: 0; }

  .panel {
    position: absolute; width: 255px; height: 255px;
    font-family: "Roboto", sans-serif; color: var(--ink);
  }
  .panel > * { position: absolute; left: 0; right: 0; text-align: center; line-height: 1; }

  .brand-disc {
    left: 77px; right: auto; top: 58px;
    width: 100px; height: 100px; border-radius: 50%;
    background: var(--charcoal);
    display: flex; align-items: center; justify-content: center;
  }
  .brand-name {
    font-family: "Roboto", sans-serif; font-weight: 500;
    color: var(--on-dark); font-size: 11px; letter-spacing: 0.2px;
  }

  .scent-band {
    left: 74px; right: auto; top: 0;
    width: 103px; height: 128px; background: var(--lime);
    display: flex; align-items: center; justify-content: center;
  }

  .hand-poured { font-size: 8.5px; font-weight: 400; top: 181px; }
  .product-name {
    font-family: "Nothing You Could Do", cursive;
    font-size: 22px; top: 188px; letter-spacing: 0.5px;
  }
  .origin { font-size: 5.6px; letter-spacing: 1.3px; top: 294px; }
  .panel--front .origin { top: 214px; }

  .panel--side .hand-poured { font-size: 7.5px; top: 187px; }
  .panel--side .product-name { font-size: 19px; top: 193px; }
  .panel--side .origin { font-size: 4.8px; letter-spacing: 1.1px; top: 216px; }

  .fragrance-list {
    top: 146px; display: flex; justify-content: center; align-items: center;
    font-family: "Nothing You Could Do", cursive;
    color: var(--lime); font-size: 12px;
  }
  .fragrance-list span { padding: 0 14px; }
  .fragrance-list span + span { border-left: 1px solid var(--lime); }

  .net-weight {
    left: auto; right: 8px; top: 241px;
    font-size: 7.5px; font-weight: 300; color: var(--muted);
  }
</style>
</head>
<body>
<main class="sheet">
  <svg class="dieline" width="1200" height="666" viewBox="0 0 1200 666" aria-hidden="true">
    <g fill="none" stroke="var(--cut-line)" stroke-width="0.9">
      <polyline points="108,79 114,52.5 358,52.5 363,79"/>
      <rect x="108" y="79" width="255" height="256"/>
      <polyline points="108,335 83,339 83,586 108,590"/>
      <rect x="108" y="335" width="1023" height="255"/>
      <line x1="363" y1="335" x2="363" y2="590"/>
      <line x1="619" y1="335" x2="619" y2="590"/>
      <line x1="875" y1="335" x2="875" y2="590"/>
    </g>
  </svg>

  <section class="panel panel--front" style="left:108px; top:79px;">
    <div class="brand-disc"><span class="brand-name">Fern &amp; Isla</span></div>
    <p class="hand-poured">Hand Poured</p>
    <h2 class="product-name">Soy Candle</h2>
    <p class="origin">MADE IN MELBOURNE</p>
  </section>

  <section class="panel panel--front" style="left:108px; top:335px;">
    <div class="brand-disc"><span class="brand-name">Fern &amp; Isla</span></div>
    <p class="hand-poured">Hand Poured</p>
    <h2 class="product-name">Soy Candle</h2>
    <p class="origin">MADE IN MELBOURNE</p>
  </section>

  <section class="panel panel--side" style="left:363px; top:335px;">
    <div class="scent-band"><span class="brand-name">Fern &amp; Isla</span></div>
    <p class="fragrance-list"><span>Lime</span><span>Elderflower</span><span>Coconut</span></p>
    <p class="hand-poured">Hand Poured</p>
    <h2 class="product-name">Soy Candle</h2>
    <p class="origin">MADE IN MELBOURNE</p>
    <p class="net-weight">300grams</p>
  </section>

  <section class="panel panel--front" style="left:619px; top:335px;">
    <div class="brand-disc"><span class="brand-name">Fern &amp; Isla</span></div>
    <p class="hand-poured">Hand Poured</p>
    <h2 class="product-name">Soy Candle</h2>
    <p class="origin">MADE IN MELBOURNE</p>
  </section>

  <section class="panel panel--side" style="left:875px; top:335px;">
    <div class="scent-band"><span class="brand-name">Fern &amp; Isla</span></div>
    <p class="fragrance-list"><span>Lime</span><span>Elderflower</span><span>Coconut</span></p>
    <p class="hand-poured">Hand Poured</p>
    <h2 class="product-name">Soy Candle</h2>
    <p class="origin">MADE IN MELBOURNE</p>
    <p class="net-weight">300grams</p>
  </section>
</main>
</body>
</html>
```